NEW YORK Plumbing/utility company 10 year anniversary business card

Looking For simple back and front business card would like to include a few things in description
We offer 24/7 emergency service
residential
commercial
industrial
municipal
services offered
Plumbing
hydro excavation
hydro jetting
Well pumps
Sewer pumps
water mains
sewer mains

```html
<!DOCTYPE html>
<html lang="en">
<head>
<meta charset="utf-8">
<title>Ridgeline Water &amp; Sewer – Business Card</title>
<link href="https://fonts.googleapis.com/css2?family=Poppins:wght@400;600&display=swap" rel="stylesheet">
<style>
  :root {
    --backdrop: #93a3b6;
    --card-light: #f2f2f2;
    --card-shade: #e2e2e2;
    --brand-blue: #1a5f9f;
    --accent-blue: #3fa6da;
    --ink: #2f2f2f;
  }
  * { box-sizing: border-box; margin: 0; padding: 0; }
  html, body { width: 1200px; height: 802px; overflow: hidden; }
  body {
    background: var(--backdrop);
    font-family: "Poppins", sans-serif;
    color: var(--ink);
    position: relative;
  }
  .card {
    position: absolute;
    left: 284px;
    width: 632px;
    height: 360px;
    background: linear-gradient(135deg, var(--card-light), var(--card-shade));
    box-shadow: 0 12px 28px rgba(30, 45, 65, 0.35);
    overflow: hidden;
  }
  .card--front { top: 26px; }
  .card--back { top: 414px; }
  .card__swoosh { position: absolute; inset: 0; width: 100%; height: 100%; }

  .wordmark {
    position: absolute;
    color: var(--brand-blue);
    font-weight: 600;
    text-align: center;
    line-height: 1;
    display: flex;
    align-items: center;
    gap: 12px;
  }
  .wordmark__dot {
    width: 26px; height: 26px;
    border-radius: 50%;
    background: var(--brand-blue);
    flex: none;
  }
  .wordmark__name { font-size: 36px; letter-spacing: 1px; }
  .wordmark__sub { font-size: 15px; letter-spacing: 3px; margin-top: 8px; }

  .card--front .wordmark { left: 56px; top: 70px; }
  .card--back .wordmark { left: 50%; top: 66px; transform: translateX(-50%); }

  .contact { position: absolute; left: 60px; list-style: none; font-size: 19px; }
  .contact li { display: flex; align-items: center; gap: 16px; height: 38px; }
  .contact svg { width: 22px; height: 22px; flex: none; }
  .contact { top: 232px; }

  .services { position: absolute; left: 348px; top: 46px; }
  .services__title { color: var(--brand-blue); font-weight: 600; font-size: 19px; margin-bottom: 6px; }
  .services__list { list-style: none; font-size: 19px; }
  .services__list li { height: 35px; display: flex; align-items: center; }
  .services__list li::before {
    content: ""; width: 8px; height: 8px; border-radius: 50%;
    background: var(--brand-blue); margin-right: 16px; margin-left: 2px;
  }

  .offerings {
    position: absolute; left: 0; right: 0; top: 222px;
    list-style: none; font-size: 20px; color: #222;
    display: grid; grid-template-columns: 1fr 1fr;
    width: 340px; margin: 0 auto; row-gap: 6px;
  }
  .offerings li { display: flex; align-items: center; white-space: nowrap; height: 30px; }
  .offerings li::before {
    content: ""; width: 8px; height: 8px; border-radius: 50%;
    background: var(--brand-blue); margin-right: 6px;
  }
  .offerings__lead { grid-column: 1 / 3; justify-content: center; margin-left: -30px; margin-right: -30px; }
  .offerings li:nth-child(4), .offerings li:nth-child(5) { padding-left: 16px; }
</style>
</head>
<body>

  <section class="card card--front" aria-label="Business card front">
    <svg class="card__swoosh" viewBox="0 0 632 360" aria-hidden="true">
      <path d="M455 360 Q570 330 632 258 L632 360 Z" fill="var(--brand-blue)"/>
      <path d="M416 360 Q530 330 602 266" fill="none" stroke="var(--accent-blue)" stroke-width="4" stroke-linecap="round"/>
    </svg>

    <div class="wordmark">
      <span class="wordmark__dot"></span>
      <div>
        <div class="wordmark__name">RIDGELINE</div>
        <div class="wordmark__sub">WATER &amp; SEWER</div>
      </div>
    </div>

    <ul class="contact">
      <li>
        <svg viewBox="0 0 24 24" fill="none" stroke="var(--brand-blue)" stroke-width="1.6" stroke-linejoin="round">
          <path d="M5 3h4l2 5-2.5 1.5a11 11 0 0 0 6 6L16 13l5 2v4a2 2 0 0 1-2 2A16 16 0 0 1 3 5a2 2 0 0 1 2-2z"/>
        </svg>
        845-555-0182
      </li>
      <li>
        <svg viewBox="0 0 24 24" fill="none" stroke="var(--brand-blue)" stroke-width="1.6">
          <rect x="2.5" y="5" width="19" height="14"/>
          <path d="M2.5 5l9.5 8 9.5-8M2.5 19l7-6.5M21.5 19l-7-6.5"/>
        </svg>
        info@ridgelinewater.com
      </li>
    </ul>

    <div class="services">
      <h2 class="services__title">Our Services</h2>
      <ul class="services__list">
        <li>Plumbing</li>
        <li>hydro excavation</li>
        <li>hydro jetting</li>
        <li>Well pumps</li>
        <li>Sewer pumps</li>
        <li>water mains</li>
        <li>sewer mains</li>
      </ul>
    </div>
  </section>

  <section class="card card--back" aria-label="Business card back">
    <svg class="card__swoosh" viewBox="0 0 632 360" aria-hidden="true">
      <path d="M0 268 Q90 338 200 360 L0 360 Z" fill="var(--brand-blue)"/>
      <path d="M24 268 Q110 330 196 358" fill="none" stroke="var(--accent-blue)" stroke-width="4" stroke-linecap="round"/>
    </svg>

    <div class="wordmark">
      <span class="wordmark__dot"></span>
      <div>
        <div class="wordmark__name">RIDGELINE</div>
        <div class="wordmark__sub">WATER &amp; SEWER</div>
      </div>
    </div>

    <ul class="offerings">
      <li class="offerings__lead">We offer 24/7 emergency service</li>
      <li>Residential</li>
      <li>Commercial</li>
      <li>Industrial</li>
      <li>Municipal</li>
    </ul>
  </section>

</body>
</html>
```